Consumer Protection Law Firm Needs a New Website

We need a new website for our law firm. We practice consumer protection law, with an emphasis on class actions. In particular, we serve consumers who are harassed by telemarketers, debt collectors, abusive companies, and financial criminals. In short, we sue big companies that do bad things to lots of people.

The lawyer is Carl Wendrow. Current website is available through www.WendrowLaw.example. Some logo files are attached.

Prefer designs that use the colors black, red, and white, per the logo. Also prefer clean, lightweight HTML5/CSS3 design rather than Wordpress. Finally, single-page type design preferred over multi-page, but flexible.

I have some limited familiarity with HTML and CSS, particularly Bootstrap, so a Bootstrap type design that I can modify myself would be ideal.

Target Market(s)

Consumers with cellular telephones.

Industry/Entity Type

Law Firm

Coding

Coded - Design and coding required

Number of Pages Required

1 page

Requirements
Must have
• - Mobile friendly, preferably without requiring separate design. In other words, a framework like Bootstrap is preferred.
• - Contact Form
• - A section for recent results
• - A section for a picture and bio of Carl Wendrow, Esq.
Nice to have
• - Animated elements that count-up and populate with numbers for things like:
• * X dollars recovered for consumers.
• * Y clients represented
• * Over Z lawsuits filed for consumers

```html
<!DOCTYPE html>
<html lang="en">
<head>
<meta charset="utf-8">
<title>Wendrow Law – Consumer Advocates</title>
<link rel="stylesheet" href="https://fonts.googleapis.com/css2?family=Open+Sans:wght@400;600;700&family=Playfair+Display:wght@400&display=swap">
<style>
:root{
  --red:#b3103b;
  --red-dark:#950a2f;
  --ink:#2b2b2b;
  --muted:#8a8a8a;
  --header:#ececec;
  --dark:#1f1b1c;
  --darker:#171415;
  --light:#eceded;
  --white:#ffffff;
}
*{box-sizing:border-box;margin:0;padding:0}
html,body{width:1200px;height:2557px;overflow:hidden;background:var(--white)}
body{font-family:"Open Sans",Arial,sans-serif;color:var(--ink);position:relative}
.abs{position:absolute}
.serif{font-family:"Playfair Display",Georgia,serif;font-weight:400}

/* header */
.site-header{left:0;top:0;width:1200px;height:105px;background:var(--header);border-top:3px solid var(--red)}
.brand{left:99px;top:31px;display:flex;align-items:center;gap:12px}
.brand-square{width:38px;height:38px;background:var(--red)}
.brand-name{font-size:30px;font-weight:600;color:var(--ink);letter-spacing:1px;line-height:1}
.nav a{position:absolute;top:39px;font-size:14px;color:#555;text-decoration:none}
.nav a.active{color:var(--red)}
.nav-tab{left:518px;top:0;width:60px;height:6px;background:var(--red);clip-path:polygon(0 0,100% 0,60% 100%,40% 100%)}

/* hero */
.hero{left:0;top:105px;width:1200px;height:600px;background:linear-gradient(90deg,#3a3530 0%,#6d6155 30%,#4a4e56 55%,#7a7268 80%,#3e3a36 100%)}
.hero-arrow{top:402px;width:20px;height:40px}
.lead-box{left:99px;top:188px;width:423px;height:358px;background:rgba(20,18,18,.82);padding:26px 31px}
.lead-box h2{font-size:25px;font-weight:400;color:var(--white);line-height:37px;margin-bottom:24px}
.field{height:43px;background:#3d3b3b;border:1px solid #555;margin-bottom:9px;padding:0 20px;font-size:14px;font-style:italic;color:#ddd;line-height:41px}
.btn{background:var(--red);color:var(--white);text-align:center;font-size:16px}
.lead-box .btn{height:44px;line-height:44px;margin-top:9px}

/* services */
.services{left:68px;top:627px;width:1064px;height:311px;background:var(--white);box-shadow:0 8px 24px rgba(0,0,0,.08)}
.services h2{position:absolute;top:54px;width:100%;text-align:center;font-size:29px;color:var(--ink)}
.service{position:absolute;top:118px;width:227px}
.service-head{display:flex;align-items:center;gap:12px;height:48px}
.service-head h3{font-size:17px;font-weight:600;color:#333}
.service p{margin-top:18px;font-size:12.5px;line-height:20px;color:var(--muted);text-align:justify}

/* intro */
.intro{left:0;top:985px;width:1200px;text-align:center}
.intro h2{font-size:29px;color:var(--ink)}
.intro .sub{margin-top:14px;font-size:13.5px;font-weight:600;color:#444}
.intro .body{margin:22px auto 0;width:910px;font-size:12px;line-height:20px;color:var(--muted)}
.intro .btn{display:block;margin:35px auto 0;width:227px;height:66px;line-height:66px;font-size:17px;font-weight:600}

/* news */
.news{left:0;top:1313px;width:1200px;height:574px;background:linear-gradient(90deg,#141212,#2a2626 50%,#141212)}
.news h2{position:absolute;top:62px;width:100%;text-align:center;color:var(--white);font-size:29px}
.news-card{position:absolute;top:136px;width:319px;color:var(--white)}
.news-thumb{height:200px}
.news-card h3{margin-top:28px;font-size:17.5px;font-weight:400;line-height:26px}
.news-date{font-size:12px;margin-left:14px;white-space:nowrap}
.news-date svg{vertical-align:-3px;margin-right:10px}
.news-card p{margin-top:16px;font-size:12.5px;line-height:25px;color:#ddd}

/* stats */
.stats{left:0;top:1887px;width:1200px;height:290px;background:linear-gradient(180deg,#e4e5e6,#f3f3f3 50%,#e1e2e3)}
.stat{position:absolute;top:55px;width:180px;height:180px;text-align:center}
.stat svg{position:absolute;left:0;top:0}
.stat-num{position:absolute;top:46px;width:100%;font-size:40px;color:var(--red)}
.stat-label{position:absolute;top:104px;width:100%;font-size:13px;line-height:20px;color:var(--red)}

/* footer */
.site-footer{left:0;top:2177px;width:1200px;height:299px;background:var(--dark);color:#999}
.site-footer h4{position:absolute;top:50px;font-size:24px;color:var(--white)}
.contact-list{position:absolute;left:99px;top:103px;width:330px;list-style:none;font-size:12px;line-height:20px}
.contact-list li{display:flex;gap:16px;margin-bottom:13px}
.contact-list svg{flex:none;margin-top:2px}
.page-list{position:absolute;left:532px;top:101px;list-style:none;font-size:12.5px}
.page-list li{height:30px;display:flex;align-items:center;gap:18px}
.page-list li::before{content:"";width:6px;height:6px;border-radius:50%;background:var(--red)}
.newsletter-input{position:absolute;left:806px;top:108px;width:294px;height:44px;background:#333031}
.social{position:absolute;left:806px;top:185px;display:flex;gap:6px}
.social span{width:17px;height:17px;background:#777}
.send-btn{position:absolute;left:975px;top:171px;width:125px;height:42px;line-height:42px;font-size:18px;font-family:"Playfair Display",Georgia,serif}
.footer-bottom{left:0;top:2476px;width:1200px;height:81px;background:var(--darker)}
.footer-bottom p{position:absolute;left:102px;top:32px;font-size:11.5px;color:#666}
</style>
</head>
<body>

<header class="site-header abs">
  <div class="brand abs"><span class="brand-square"></span><span class="brand-name">WENDROW LAW</span></div>
  <span class="nav-tab abs"></span>
  <nav class="nav">
    <a class="active" style="left:535px">Home</a>
    <a style="left:617px">The Firm</a>
    <a style="left:716px">Practice Areas</a>
    <a style="left:849px">News</a>
    <a style="left:927px">FAQ</a>
    <a style="left:996px">Contact</a>
    <svg class="abs" style="left:1087px;top:43px" width="14" height="14" viewBox="0 0 14 14"><circle cx="6" cy="6" r="4.5" fill="none" stroke="#555" stroke-width="2"/><line x1="9.5" y1="9.5" x2="13" y2="13" stroke="#555" stroke-width="2"/></svg>
  </nav>
</header>

<section class="hero abs" role="img" aria-label="Photo of an attorney in a suit meeting a client across a desk"></section>
<svg class="hero-arrow abs" style="left:34px" viewBox="0 0 20 40"><polyline points="18,2 2,20 18,38" fill="none" stroke="rgba(255,255,255,.5)" stroke-width="2"/></svg>
<svg class="hero-arrow abs" style="left:1148px" viewBox="0 0 20 40"><polyline points="2,2 18,20 2,38" fill="none" stroke="rgba(255,255,255,.5)" stroke-width="2"/></svg>

<form class="lead-box abs">
  <h2>Telephone harassment is a serious violation of your rights.</h2>
  <div class="field">Tel No :</div>
  <div class="field">First Name :</div>
  <div class="field">Last Name:</div>
  <div class="btn">Get Your Free Consultation</div>
</form>

<section class="services abs">
  <h2 class="serif">Our Service</h2>
  <div class="service" style="left:31px">
    <div class="service-head">
      <svg width="52" height="44" viewBox="0 0 52 44"><circle cx="18" cy="12" r="9" fill="var(--red)"/><path d="M2 42c0-12 7-18 16-18s16 6 16 18z" fill="var(--red)"/><circle cx="35" cy="14" r="8" fill="var(--red)"/><path d="M24 42c2-10 6-15 11-15 8 0 15 5 15 15z" fill="var(--red)"/></svg>
      <h3>Telemarketers</h3>
    </div>
    <p>At vero eos et accusamus et iusto odio dignissimos ducimus qui blanditiis praesentium voluptatum deleniti atque corrupti quos dolores et quas</p>
  </div>
  <div class="service" style="left:290px">
    <div class="service-head">
      <svg width="50" height="44" viewBox="0 0 50 44"><path d="M2 8h14l4 5h26v29H2z" fill="var(--red)"/><rect x="10" y="3" width="28" height="20" fill="#fff" stroke="var(--red)" stroke-width="2"/><path d="M2 18h44v24H2z" fill="var(--red)"/></svg>
      <h3>Debt collectors</h3>
    </div>
    <p>At vero eos et accusamus et iusto odio dignissimos ducimus qui blanditiis praesentium voluptatum deleniti atque corrupti quos dolores et quas</p>
  </div>
  <div class="service" style="left:549px">
    <div class="service-head">
      <svg width="56" height="44" viewBox="0 0 56 44"><rect x="6" y="6" width="22" height="10" transform="rotate(35 17 11)" fill="var(--red)"/><line x1="22" y1="18" x2="46" y2="36" stroke="var(--red)" stroke-width="4"/><rect x="2" y="36" width="26" height="6" fill="var(--red)"/></svg>
      <h3>Abusive companies</h3>
    </div>
    <p>At vero eos et accusamus et iusto odio dignissimos ducimus qui blanditiis praesentium voluptatum deleniti atque corrupti quos dolores et quas</p>
  </div>
  <div class="service" style="left:808px">
    <div class="service-head">
      <svg width="48" height="44" viewBox="0 0 48 44"><circle cx="22" cy="24" r="18" fill="none" stroke="var(--red)" stroke-width="4"/><circle cx="22" cy="24" r="10" fill="none" stroke="var(--red)" stroke-width="4"/><circle cx="22" cy="24" r="3" fill="var(--red)"/><line x1="22" y1="24" x2="42" y2="4" stroke="var(--red)" stroke-width="3"/><path d="M38 2l8 0-2 6z" fill="var(--red)"/></svg>
      <h3>Financial criminals</h3>
    </div>
    <p>At vero eos et accusamus et iusto odio dignissimos ducimus qui blanditiis praesentium voluptatum deleniti atque corrupti quos dolores et quas</p>
  </div>
</section>

<section class="intro abs">
  <h2 class="serif">Are you being harassed by debt collectors?</h2>
  <p class="sub">Unlawful telephone harassment is a serious violation of your rights. Don't stand for it.&nbsp; Contact attorney Carl Wendrow today.</p>
  <p class="body">I must explain to you how all this mistaken idea of denouncing pleasure and praising pain was born and I will give you a complete account of the system, and expound the actual teachings of the great explorer of the truth, the master-builder of human happiness. No one rejects, dislikes, or avoids pleasure itself, because it is pleasure, but because those who do not know how to pursue pleasure rationally encounter consequences that are extremely painful.</p>
  <span class="btn">Free Consultation</span>
</section>

<section class="news abs">
  <h2 class="serif">Latest News</h2>
  <article class="news-card" style="left:99px">
    <div class="news-thumb" role="img" aria-label="Photo of a traffic light with a photo enforced sign" style="background:linear-gradient(180deg,#d8dadc,#b9bcbf)"></div>
    <h3>Carl Wendrow, Esq. Wins Ruling in Florida Supreme Court that Pre-July 1, 2010 Red Light Cameras Illegal <span class="news-date"><svg width="14" height="14" viewBox="0 0 14 14"><circle cx="7" cy="7" r="6" fill="#fff"/><path d="M7 3.5V7h3" stroke="#222" stroke-width="1.5" fill="none"/></svg>June 13, 2014</span></h3>
    <p>Carl Wendrow, Esq. Obtains Ruling from Florida Supreme Court that Red Light Camera Programs from Before July 1, 2010...</p>
  </article>
  <article class="news-card" style="left:440px">
    <div class="news-thumb" role="img" aria-label="Photo of a judge's gavel resting on a book" style="background:linear-gradient(135deg,#8a7d6c,#5f564b)"></div>
    <h3>Carl Wendrow, Esq. Obtains $63,000.00 Judgment Against Debt Collector for Harassment <span class="news-date"><svg width="14" height="14" viewBox="0 0 14 14"><circle cx="7" cy="7" r="6" fill="#fff"/><path d="M7 3.5V7h3" stroke="#222" stroke-width="1.5" fill="none"/></svg>May 9, 2014</span></h3>
    <p>On May 1, 2014, Carl Wendrow, Esq. obtained partial summary judgment against Meridian Collection Services, Inc., for...</p>
  </article>
  <article class="news-card" style="left:783px">
    <div class="news-thumb" role="img" aria-label="Photo of a red corporate bank building sign" style="background:linear-gradient(135deg,#5a4a48,#b0202a 60%,#c8343b)"></div>
    <h3>Record Settlement in Keystone National Bank TCPA Class Action</h3>
    <p style="margin-top:42px"><span class="news-date" style="margin-left:0"><svg width="14" height="14" viewBox="0 0 14 14"><circle cx="7" cy="7" r="6" fill="#fff"/><path d="M7 3.5V7h3" stroke="#222" stroke-width="1.5" fill="none"/></svg>January 26, 2014</span><br>It appears Keystone National Bank will be paying over $32 million in an effort to settle six pending TCPA class action...</p>
  </article>
</section>

<section class="stats abs">
  <div class="stat" style="left:171px">
    <svg width="180" height="180" viewBox="0 0 180 180"><path d="M90 2A88 88 0 1 1 2 90" fill="none" stroke="var(--red)" stroke-width="3"/></svg>
    <div class="stat-num">526</div>
    <div class="stat-label">X dollars recovered<br>for consumers.</div>
  </div>
  <div class="stat" style="left:510px">
    <svg width="180" height="180" viewBox="0 0 180 180"><path d="M178 90A88 88 0 1 1 90 2" fill="none" stroke="var(--red)" stroke-width="3"/></svg>
    <div class="stat-num">256</div>
    <div class="stat-label">Y clients represented</div>
  </div>
  <div class="stat" style="left:843px">
    <svg width="180" height="180" viewBox="0 0 180 180"><path d="M90 2A88 88 0 1 1 12 131" fill="none" stroke="var(--red)" stroke-width="3"/></svg>
    <div class="stat-num">625</div>
    <div class="stat-label">Over Z lawsuits filed<br>for consumers</div>
  </div>
</section>

<footer class="site-footer abs">
  <h4 class="serif" style="left:99px">Contact Us</h4>
  <ul class="contact-list">
    <li><svg width="14" height="14" viewBox="0 0 14 14"><path d="M1 6l12-5-5 12-1.5-5.5z" fill="var(--red)"/></svg><span>Law Office of Carl Wendrow, Esq., 4410 Harbor View Blvd., Ste 210, Coral Point, FL 33099</span></li>
    <li><svg width="14" height="14" viewBox="0 0 14 14"><path d="M3 1l3 3-1.5 2c1 2 2 3 3.5 3.5L10 8l3 3-2 2C6 13 1 8 1 3z" fill="var(--red)"/></svg><span>1.855.555.0146 / 1.954.555.0141</span></li>
    <li><svg width="14" height="14" viewBox="0 0 14 14"><rect x="1" y="5" width="12" height="8" fill="var(--red)"/><rect x="4" y="1" width="6" height="5" fill="var(--red)"/></svg><span>1.954.555.0144</span></li>
    <li><svg width="14" height="14" viewBox="0 0 14 14"><rect x="1" y="3" width="12" height="9" fill="none" stroke="var(--red)" stroke-width="1.5"/><path d="M1 3l6 5 6-5" fill="none" stroke="var(--red)" stroke-width="1.5"/></svg><span>info@wendrowlaw.example</span></li>
  </ul>
  <h4 class="serif" style="left:532px">All Site Pages</h4>
  <ul class="page-list">
    <li>Home</li><li>The Firm</li><li>Practice Areas</li><li>News</li><li>FAQ</li>
  </ul>
  <h4 class="serif" style="left:806px">Newsletter Sign Up</h4>
  <div class="newsletter-input"></div>
  <div class="social"><span></span><span></span><span></span><span></span><span></span></div>
  <div class="send-btn btn">Send Now</div>
</footer>
<div class="footer-bottom abs"><p>Copyrights@2016wendrowlaw . all rights reserved</p></div>

</body>
</html>
```